Vireo M.K. - Diagnostic Ultrasound Flyer

About US
Vireo M.K. is a concierge ultrasound company that provides onsite or offsite diagnostic ultrasounds. We have over 14 years experience in sonography, business management, and customer service. We offer both the physician and patient flexibility, convenience, and access to timely services.

We provide ultrasounds for the following specialties:
Obstetrics/Gynecology
Abdominal
Small Parts
Vascular

Company Features:
1. Onsite or Offsite Scans
2. Images Available Immediately for Referring Physician and Patient
3. Flexible Options for Ultrasound Interpretation/Billing
4. Access to Interpreting Radiologist
5. Final Report Process - 1-2 Business Days/ 1 hour for STAT.
6. PACS Storage with Secure Access.

We need a place to add in our contact information (address, email, website, phone)

We already have a logo and would like to use it ( they are attached). We would the colors to match the logo colors....maybe lighter version of yellow and blue.

```html
<!DOCTYPE html>
<html lang="en">
<head>
<meta charset="utf-8">
<title>Vireo M.K. – Diagnostic Ultrasound Flyer</title>
<link rel="stylesheet" href="https://fonts.googleapis.com/css2?family=Bebas+Neue&family=Poppins:wght@400;500;600;700&display=swap">
<style>
:root{
  --navy:#2218b4;
  --navy-deep:#1a1296;
  --yellow:#fbb829;
  --ink:#16163a;
  --paper:#ffffff;
  --mist:#eef1f8;
  --stage:#e9e9ec;
}
*{margin:0;padding:0;box-sizing:border-box}
html,body{width:1200px;height:2342px;overflow:hidden;background:var(--stage)}
body{position:relative;font-family:'Poppins',sans-serif;color:var(--ink)}
.flyer{position:absolute;left:50px;top:458px;width:1100px;height:1425px;background:var(--paper);overflow:hidden;box-shadow:0 10px 30px rgba(0,0,0,.12)}
.abs{position:absolute}
svg.layer{position:absolute;left:0;display:block}

/* header */
.brand{left:50px;top:68px;display:flex;align-items:center;gap:14px;font-weight:700;font-size:50px;letter-spacing:2px;color:var(--navy);line-height:1}
.brand-dot{width:18px;height:18px;border-radius:50%;background:var(--yellow)}

/* hero */
.hero-title{left:48px;top:178px;font-family:'Bebas Neue',sans-serif;font-size:196px;line-height:1;color:var(--yellow);letter-spacing:-2px}
.hero-sub{left:50px;top:336px;font-family:'Bebas Neue',sans-serif;font-size:72px;line-height:1;color:#fff;letter-spacing:-.5px}
.hero-rule{left:50px;top:404px;width:90px;height:4px;background:linear-gradient(90deg,var(--yellow),rgba(251,184,41,0))}
.hero-tag{left:47px;top:427px;font-weight:600;font-size:23px;line-height:29px;color:#fff}

/* content */
.content{left:0;top:522px;width:1100px;height:486px;background:linear-gradient(180deg,var(--mist),#fff 60%,var(--mist))}
.pill{display:flex;align-items:center;height:36px;border-radius:8px;background:var(--yellow);color:var(--navy);font-weight:600;font-size:24px}
.pill .pill-icon{width:36px;height:36px;border-radius:8px;background:var(--navy);display:flex;align-items:center;justify-content:center;margin-right:12px}
.about{left:50px;top:26px;width:190px}
.offer{left:50px;top:271px;width:190px}
.features{left:555px;top:26px;width:296px}
.about-text{left:50px;top:73px;width:445px;font-size:17.6px;line-height:21.8px;color:var(--ink)}
.list{list-style:none}
.list li{position:absolute;display:flex;align-items:center;font-size:19.5px;line-height:22px;color:var(--ink);white-space:nowrap}
.list li .box{flex:none;width:32px;height:32px;border:2px solid var(--navy);border-left-width:4px;background:var(--yellow);margin-right:22px;display:flex;align-items:center;justify-content:center}
.list li .box i{width:14px;height:14px;border:2px solid var(--navy);border-radius:2px;display:block}
.exp-box{left:567px;top:376px;width:463px;height:42px;background:var(--navy);border-radius:4px;color:var(--yellow);font-family:'Bebas Neue',sans-serif;font-size:36px;line-height:44px;text-align:center;letter-spacing:.3px}
.exp-row{left:555px;top:428px;width:500px;font-weight:500;font-size:20.5px;line-height:23px;color:var(--ink)}
.exp-row span{position:absolute;display:flex;gap:8px;white-space:nowrap}
.tick{flex:none;width:16px;height:16px;margin-top:5px}

/* specialties */
.spec-head{left:695px;top:1032px;font-weight:600;font-size:20.5px;line-height:24px;color:#fff}
.spec-head em{font-style:normal;color:var(--yellow)}
.spec-list{left:700px;top:1092px;font-size:19.5px;line-height:29px;color:#fff;list-style:none}
.spec-list li{display:flex;gap:14px;align-items:center}
.spec-list .tick{margin-top:0}

/* contact strip */
.contact-tab{left:56px;top:1258px;font-family:'Bebas Neue',sans-serif;font-size:44px;line-height:1;color:var(--navy)}
.contact-tab small{display:block;font-family:'Poppins',sans-serif;font-weight:600;font-size:13px;letter-spacing:.4px;margin-top:-2px}
.hours{left:308px;top:1278px;width:470px;font-family:'Bebas Neue',sans-serif;font-size:31px;line-height:1;color:var(--navy);white-space:nowrap}
.opening{left:793px;top:1268px;width:250px;height:36px;border-radius:18px;background:var(--yellow);display:flex;overflow:hidden}
.opening b{flex:1;font-size:16px;font-weight:700;color:var(--navy);text-align:center;line-height:36px}
.opening span{width:115px;background:var(--navy);color:#fff;border-radius:18px;font-family:'Bebas Neue',sans-serif;font-size:30px;line-height:38px;text-align:center}

/* footer */
.footer-line{left:0;top:1322px;width:1100px;height:8px;background:var(--yellow)}
.footer{left:0;top:1330px;width:1100px;height:95px;background:var(--navy);color:#fff}
.phone{left:52px;top:22px;display:flex;align-items:center;gap:14px;font-weight:500;font-size:34px;line-height:40px}
.web{left:396px;top:16px;font-size:18.5px;line-height:24px;font-weight:500}
.addr{left:673px;top:18px;font-size:17.5px;line-height:23px;font-weight:500}
.web div,.addr{display:flex;gap:14px}
.ico{flex:none}
</style>
</head>
<body>
<main class="flyer">

  <svg class="layer" style="top:0" width="1100" height="522" viewBox="0 0 1100 522">
    <defs>
      <linearGradient id="clinicTone" x1="0" y1="0" x2="1" y2="1">
        <stop offset="0" stop-color="#d9dde6"/>
        <stop offset=".55" stop-color="#b9c0cf"/>
        <stop offset="1" stop-color="#8b7b72"/>
      </linearGradient>
    </defs>
    <path d="M1100 52 H575 Q538 52 518 88 L480 152" fill="none" stroke="var(--yellow)" stroke-width="8"/>
    <g role="img" aria-label="Photo of a smiling sonographer scanning an expectant mother, with a baby ultrasound image on the monitor">
      <path d="M560 70 H1100 V502 H480 Z" fill="url(#clinicTone)"/>
    </g>
    <path d="M520 152 Q557 152 574 188 L712 522" fill="none" stroke="var(--yellow)" stroke-width="7"/>
    <path d="M0 152 H500 Q536 152 553 188 L690 522 H0 Z" fill="var(--navy)"/>
    <rect x="0" y="500" width="1100" height="22" fill="var(--navy)"/>
  </svg>

  <div class="abs brand"><span>Vireo M.K.</span><span class="brand-dot"></span></div>
  <h1 class="abs hero-title">3D/4D</h1>
  <h2 class="abs hero-sub">BABY ULTRASOUND</h2>
  <div class="abs hero-rule"></div>
  <p class="abs hero-tag">Diagnostic Medical Ultrasounds &amp; 3D/4D<br>Baby Ultrasounds</p>

  <section class="abs content">
    <div class="abs pill about"><span class="pill-icon"><svg width="20" height="20" viewBox="0 0 20 20"><circle cx="10" cy="10" r="8.5" fill="none" stroke="#fff" stroke-width="1.5"/><circle cx="10" cy="8" r="3" fill="none" stroke="#fff" stroke-width="1.5"/><path d="M4.5 15.5 Q10 10.5 15.5 15.5" fill="none" stroke="#fff" stroke-width="1.5"/></svg></span>About us</div>
    <p class="abs about-text">We have over 15 years in sonography, business management, and customer service and provide a variety of sonography services. Our mission is to be a customer centric provider while focusing on flexibility, quality, and speed. We specialize in diagnostic/non-diagnostic obstetric ultrasounds and 2D, 3D, 4D, and HD Live baby ultrasounds.</p>

    <div class="abs pill offer"><span class="pill-icon"><svg width="20" height="20" viewBox="0 0 20 20"><path d="M3 13 H8 L12 15 H17" fill="none" stroke="#fff" stroke-width="1.5"/><circle cx="10" cy="7" r="3.5" fill="none" stroke="#fff" stroke-width="1.5"/></svg></span>We offer</div>
    <ul class="list">
      <li style="left:52px;top:317px"><span class="box"><i></i></span>Physician and patient flexibility</li>
      <li style="left:52px;top:360px"><span class="box"><i></i></span>Convenience</li>
      <li style="left:52px;top:402px"><span class="box"><i></i></span>Access to timely services</li>
    </ul>

    <div class="abs pill features"><span class="pill-icon"><svg width="20" height="20" viewBox="0 0 20 20"><rect x="3" y="3" width="14" height="14" rx="2" fill="none" stroke="#fff" stroke-width="1.5"/><circle cx="10" cy="10" r="3" fill="none" stroke="#fff" stroke-width="1.5"/></svg></span>Company Features</div>
    <ul class="list">
      <li style="left:562px;top:74px"><span class="box"><i></i></span>Onsite or Offsite Scans</li>
      <li style="left:562px;top:114px"><span class="box"><i></i></span>Images Available Immediately for Referring<br>Physician and Patient</li>
      <li style="left:562px;top:168px"><span class="box"><i></i></span>Flexible Options for Ultrasound Interpretation<br>/Billing</li>
      <li style="left:562px;top:224px"><span class="box"><i></i></span>Access to Interpreting Radiologist</li>
      <li style="left:562px;top:268px"><span class="box"><i></i></span>Final Report Process - 1-2 Business Days/<br>1 hour for STAT.</li>
      <li style="left:562px;top:326px"><span class="box"><i></i></span>PACS Storage with Secure Access</li>
    </ul>

    <div class="abs exp-box">14 YEARS EXPERIENCE IN</div>
    <div class="abs exp-row">
      <span style="left:0;top:0"><svg class="tick" viewBox="0 0 16 16"><path d="M2 8 L6 13 L14 2" fill="none" stroke="var(--navy)" stroke-width="2.5"/></svg>Sonography</span>
      <span style="left:170px;top:-2px"><svg class="tick" viewBox="0 0 16 16"><path d="M2 8 L6 13 L14 2" fill="none" stroke="var(--navy)" stroke-width="2.5"/></svg>Business<br>management</span>
      <span style="left:352px;top:-2px"><svg class="tick" viewBox="0 0 16 16"><path d="M2 8 L6 13 L14 2" fill="none" stroke="var(--navy)" stroke-width="2.5"/></svg>Customer<br>service</span>
    </div>
  </section>

  <svg class="layer" style="top:1008px" width="1100" height="228" viewBox="0 0 1100 228">
    <defs>
      <linearGradient id="scanTone" x1="0" y1="0" x2="1" y2="0">
        <stop offset="0" stop-color="#c8d2de"/>
        <stop offset=".5" stop-color="#e6e9ee"/>
        <stop offset="1" stop-color="#d8c3b8"/>
      </linearGradient>
    </defs>
    <g role="img" aria-label="Photo of a sonographer at an ultrasound machine examining a patient lying on a bed">
      <rect x="0" y="0" width="640" height="228" fill="url(#scanTone)"/>
    </g>
    <path d="M553 0 L632 125 L572 228" fill="none" stroke="var(--yellow)" stroke-width="8"/>
    <path d="M568 0 H1100 V228 H588 L648 125 Z" fill="var(--navy)"/>
  </svg>

  <p class="abs spec-head">We provide <em>ultrasounds</em> for the<br>following specialties</p>
  <ul class="abs spec-list">
    <li><svg class="tick" viewBox="0 0 16 16"><path d="M2 8 L6 13 L14 2" fill="none" stroke="var(--yellow)" stroke-width="2.5"/></svg>Obstetrics/Gynecology</li>
    <li><svg class="tick" viewBox="0 0 16 16"><path d="M2 8 L6 13 L14 2" fill="none" stroke="var(--yellow)" stroke-width="2.5"/></svg>Abdominal</li>
    <li><svg class="tick" viewBox="0 0 16 16"><path d="M2 8 L6 13 L14 2" fill="none" stroke="var(--yellow)" stroke-width="2.5"/></svg>Small Parts</li>
    <li><svg class="tick" viewBox="0 0 16 16"><path d="M2 8 L6 13 L14 2" fill="none" stroke="var(--yellow)" stroke-width="2.5"/></svg>Vascular</li>
  </ul>

  <svg class="layer" style="top:1236px" width="1100" height="94" viewBox="0 0 1100 94">
    <path d="M0 0 H262 Q278 0 285 14 L300 86 H0 Z" fill="var(--yellow)"/>
  </svg>
  <div class="abs contact-tab">CONTACT US TO<small>MAKE AN APPOINTMENTS</small></div>
  <div class="abs hours">WEEKDAYS, WEEKENDS, AND EVENINGS AVAILABLE</div>
  <div class="abs opening"><b>OPENING AT</b><span>9:00 AM</span></div>

  <div class="abs footer-line"></div>
  <footer class="abs footer">
    <div class="abs phone"><svg class="ico" width="34" height="34" viewBox="0 0 24 24"><path d="M6.6 10.8a15.1 15.1 0 0 0 6.6 6.6l2.2-2.2c.3-.3.7-.4 1-.2 1.1.4 2.3.6 3.6.6.6 0 1 .4 1 1V20c0 .6-.4 1-1 1C10.6 21 3 13.4 3 4c0-.6.4-1 1-1h3.5c.6 0 1 .4 1 1 0 1.3.2 2.5.6 3.6.1.3 0 .7-.2 1z" fill="var(--yellow)"/></svg>(555) 214-0387</div>
    <div class="abs web">
      <div><svg class="ico" width="20" height="20" viewBox="0 0 20 20" style="margin-top:2px"><rect x="1.5" y="4" width="17" height="12" fill="none" stroke="var(--yellow)" stroke-width="1.8"/><path d="M1.5 4 L10 11 L18.5 4" fill="none" stroke="var(--yellow)" stroke-width="1.8"/></svg>info@vireo-mk.com</div>
      <div><svg class="ico" width="20" height="20" viewBox="0 0 20 20" style="margin-top:2px"><circle cx="10" cy="10" r="8" fill="none" stroke="var(--yellow)" stroke-width="1.8"/><path d="M2 10 H18 M10 2 Q5 10 10 18 M10 2 Q15 10 10 18" fill="none" stroke="var(--yellow)" stroke-width="1.5"/></svg>www.vireo-mk.com</div>
    </div>
    <div class="abs addr"><svg class="ico" width="18" height="24" viewBox="0 0 18 24"><path d="M9 1C4.6 1 1 4.5 1 8.8 1 14.5 9 23 9 23s8-8.5 8-14.2C17 4.5 13.4 1 9 1z" fill="none" stroke="var(--yellow)" stroke-width="2"/><circle cx="9" cy="9" r="3" fill="var(--yellow)"/></svg><span>4180 Larkspur Park Drive Suite B2<br>Fairmont, MD 20999 USA</span></div>
  </footer>

</main>
</body>
</html>
```